Labels designs for a new coffee brand (Vestro Coffee)

We looking for a coffee label design for our coffee Brand, VESTRO COFFE, attached is the logo. We are bringing out to the market 3 Premium blends
1. Colombian Popayan
2. Gourmet Expresso Blend
3. Brazilian Santos

We like something that looks high quality yet modern, the bags we are using is black matte, we are starting with labels and look in the near future to print our own labels .

We want the labels for the 3 coffees to have the similar look and feel but to be uniquely identified by its design (Colombian, Brazilian, espresso) This is beig sold as a set so we want it to have a similar label feeling but that each is identify as its unique product (colombian, expresso, brazilian blend.

This project is for labels that will be used on a black matte bag, is for a 16 oz bag,

Attached is a sample of the bag color.

Size Requirements:
Maintain a 2:3 aspect ratio for the image file
The label will be 4" wide and 6" tall (we also want to print some 3X4)
Recommended image size is 1600px X 2400px

I will provide upc later

www.vestrocoffee.example pw 48071 this is the test site not live yet but you can get a feel of the brand
Updates

Ay my daughters volleyball tournament I need extra time to review

Target Market(s)

coffee drinkers

Industry/Entity Type

coffee

Requirements
Must have
• Creativity, unique, eye catchy,

```html
<!DOCTYPE html>
<html lang="en">
<head>
<meta charset="utf-8">
<title>Vestro Coffee – Gourmet Expresso Blend Label</title>
<link rel="stylesheet" href="https://fonts.googleapis.com/css2?family=Montserrat:wght@500;600&family=Rye&family=Roboto+Slab:wght@400&family=Yellowtail&display=swap">
<style>
  :root {
    --backdrop: #fde9d2;
    --paper: #ffffff;
    --olive-dark: #6c684b;
    --olive-light: #aaa486;
    --brand: #9a9475;
    --ink: #2a2a2a;
    --rule: #8a5127;
    --earth: #8e5a2e;
    --earth-deep: #7d4c24;
    --cream: #fbf3e8;
  }
  * { margin: 0; padding: 0; box-sizing: border-box; }
  html, body { width: 1200px; height: 917px; overflow: hidden; }
  body { background: var(--backdrop); position: relative; font-family: "Roboto Slab", serif; }

  .label {
    position: absolute; left: 330px; top: 22px;
    width: 540px; height: 810px;
    background: var(--paper);
    box-shadow: 0 6px 14px rgba(90, 60, 30, .18);
    overflow: hidden;
  }
  .label__pattern {
    position: absolute; left: 0; top: 0; width: 100%; height: 48px;
    background: linear-gradient(90deg, #8e5628, #a9692f 50%, #8e5628);
  }
  .brand {
    position: absolute; left: 0; right: 0; top: 100px;
    display: flex; justify-content: center; align-items: center; gap: 16px;
    color: var(--brand);
  }
  .brand__mark { width: 44px; height: 44px; border-radius: 50%; background: var(--brand); }
  .brand__name {
    font-family: "Montserrat", sans-serif; font-weight: 600;
    font-size: 58px; letter-spacing: 6px; line-height: 1;
  }
  .blend {
    position: absolute; left: 62px; width: 405px; top: 212px; height: 66px;
    border-top: 2px solid var(--rule); border-bottom: 2px solid var(--rule);
  }
  .blend svg, .title svg { display: block; }
  .title { position: absolute; left: 62px; top: 292px; width: 420px; height: 172px; }
  .tagline {
    position: absolute; left: 0; right: 0; top: 470px; text-align: center;
    font-family: "Yellowtail", cursive; font-size: 33px; color: var(--ink);
  }

  .details {
    position: absolute; left: 0; right: 0; bottom: 0; height: 240px;
    background: radial-gradient(ellipse at 70% 40%, var(--earth), var(--earth-deep));
    color: var(--cream);
  }
  .details__inner { position: absolute; left: 102px; width: 334px; top: 22px; }
  .details__grade {
    font-family: "Montserrat", sans-serif; font-weight: 600;
    font-size: 21.5px; letter-spacing: 1.2px; text-align: center;
    padding-bottom: 8px; border-bottom: 1.5px solid var(--cream);
  }
  .roast {
    display: flex; align-items: center; justify-content: space-between;
    padding: 8px 0 7px; border-bottom: 1.5px solid var(--cream);
    font-size: 15px; line-height: 1.15;
  }
  .roast__scale { display: flex; gap: 20px; }
  .dot { width: 14px; height: 14px; border: 1.3px solid var(--cream); border-radius: 50%; }
  .grind { display: flex; border-bottom: 1.5px solid var(--cream); font-size: 15px; letter-spacing: .8px; }
  .grind__option { flex: 1; display: flex; align-items: center; gap: 14px; padding: 9px 4px; }
  .grind__option + .grind__option { border-left: 1.5px solid var(--cream); padding-left: 40px; }
  .facts { display: flex; gap: 80px; padding: 10px 0 9px; border-bottom: 1.5px solid var(--cream); font-size: 15px; }
  .site { text-align: center; padding-top: 8px; font-size: 15.5px; letter-spacing: 1px; }

  .caption {
    position: absolute; left: 0; right: 0; top: 846px; text-align: center;
    font-family: "Montserrat", sans-serif; font-weight: 500; font-size: 27px; color: #111;
  }
</style>
</head>
<body>
  <article class="label">
    <div class="label__pattern" role="img" aria-label="Repeating coffee bean pattern band"></div>

    <header class="brand">
      <span class="brand__mark"></span>
      <span class="brand__name">VESTRO</span>
    </header>

    <div class="blend">
      <svg width="405" height="62" viewBox="0 0 405 62">
        <text x="202" y="48" text-anchor="middle" textLength="385" lengthAdjust="spacingAndGlyphs"
              font-family="Rye, serif" font-size="44" fill="#2a2a2a">GOURMET EXPRESSO</text>
      </svg>
    </div>

    <div class="title">
      <svg width="420" height="172" viewBox="0 0 420 172">
        <defs>
          <linearGradient id="olive" x1="0" x2="1" y1="0" y2="0">
            <stop offset="0" stop-color="#6c684b"/>
            <stop offset=".55" stop-color="#aaa486"/>
            <stop offset="1" stop-color="#6c684b"/>
          </linearGradient>
        </defs>
        <text x="212" y="166" text-anchor="middle" textLength="410" lengthAdjust="spacingAndGlyphs"
              font-family="Rye, serif" font-size="150" fill="#57533c" opacity=".55">COFFEE</text>
        <text x="208" y="162" text-anchor="middle" textLength="410" lengthAdjust="spacingAndGlyphs"
              font-family="Rye, serif" font-size="150" fill="url(#olive)">COFFEE</text>
      </svg>
    </div>

    <p class="tagline">Premium Coffee, Roasted fresh daily</p>

    <section class="details" role="img" aria-label="Brown panel with faint coffee plant illustration">
      <div class="details__inner">
        <p class="details__grade">100% ARABICA COFFEE</p>
        <div class="roast">
          <span>Light<br>Roast</span>
          <span class="roast__scale">
            <span class="dot"></span><span class="dot"></span><span class="dot"></span>
            <span class="dot"></span><span class="dot"></span><span class="dot"></span>
          </span>
          <span>Dark<br>Roast</span>
        </div>
        <div class="grind">
          <span class="grind__option"><span class="dot"></span>GROUND</span>
          <span class="grind__option"><span class="dot"></span>WHOLE BEAN</span>
        </div>
        <div class="facts">
          <span>Net Wt</span>
          <span>Roasted on :</span>
        </div>
        <p class="site">www.vestrocoffee.example</p>
      </div>
    </section>
  </article>

  <p class="caption">Gourmet Expresso Blend</p>
</body>
</html>
```